Medical Device Company needs website

We are a start-up medical device company looking to sell boot (foot) and brace (ankle) products on Shopwell. We are still working on the name but you can use Tavrix as a placeholder- no logo yet)

Website information:
- Look: modern/tech with clean lines and symmetry.
- Colors: teal, white, black, and greys.
- Headers: home, shop, about us, help, blog
- Icons (upper right): search, my account and shopping cart
-place to sign up for newsletter

```html
<!DOCTYPE html>
<html lang="en">
<head>
<meta charset="utf-8">
<title>Tavrix — Home</title>
<link href="https://fonts.googleapis.com/css2?family=Archivo:wght@400;500;700&display=swap" rel="stylesheet">
<style>
:root{
  --ink:#2b2839;
  --text:#4f4d58;
  --muted:#6b6a73;
  --teal:#33d1d3;
  --teal-soft:#8fe3e6;
  --tint:#e2f6f9;
  --base:#f3f3f3;
  --white:#ffffff;
  --line:#e4e6e8;
}
*{margin:0;padding:0;box-sizing:border-box}
html,body{width:945px;height:1200px;overflow:hidden}
body{position:relative;font-family:"Archivo",Arial,sans-serif;color:var(--ink);background:var(--base)}
.abs{position:absolute}
.announcement{left:0;top:0;width:945px;height:24px;background:var(--ink);color:var(--white);font-size:10px;font-weight:500;display:flex;align-items:center;justify-content:center;letter-spacing:.3px}
.announcement svg{position:absolute;top:8px}
.site-header{left:0;top:24px;width:945px;height:84px;background:linear-gradient(180deg,#f2f5f6 0%,var(--tint) 100%)}
.brand{left:0;width:945px;top:17px;text-align:center;font-size:15px;font-weight:500;letter-spacing:.6px;color:var(--ink)}
.nav{left:0;width:945px;top:53px;display:flex;justify-content:center;gap:15px;font-size:9px;color:var(--muted)}
.nav .current{color:var(--ink);text-decoration:underline;text-underline-offset:2px}
.hero{left:0;top:108px;width:945px;height:465px;background:linear-gradient(180deg,var(--base) 0%,var(--tint) 100%)}
.hero-media{left:343px;top:15px;width:468px;height:428px;border-radius:8px;background:linear-gradient(160deg,#eef5f5,#f4f4f4 60%,#eef4f4);box-shadow:0 6px 18px rgba(0,0,0,.08)}
.hero-card{left:135px;top:51px;width:233px;height:356px;border-radius:10px;background:linear-gradient(160deg,#e0f5f8 0%,#f1f4f4 55%,#e3f6f9 100%)}
.hero-title{left:178px;top:86px;font-size:31px;line-height:36.5px;font-weight:700;color:var(--ink)}
.hero-copy{left:178px;top:247px;width:152px;font-size:10.3px;line-height:17.7px;color:var(--text)}
.btn{left:178px;top:337px;width:83px;height:28px;border-radius:5px;background:var(--ink);color:var(--white);font-size:9.5px;font-weight:500;display:flex;align-items:center;justify-content:center;letter-spacing:.3px}
.product-visual{left:517px;top:111px;width:202px;height:262px;border-radius:40px 30px 20px 20px;background:linear-gradient(180deg,#e4e5ea 0%,#d2d4dc 65%,#3fd0d3 96%,#e9f2f2 100%)}
.feature{width:75px;height:60px;border:1.5px solid var(--teal-soft);border-radius:7px;background:rgba(240,250,250,.8);display:flex;flex-direction:column;align-items:center;justify-content:center;gap:5px;font-size:9px;color:var(--text)}
.featured{left:0;top:573px;width:945px;height:359px;background:linear-gradient(180deg,var(--base) 0%,var(--tint) 100%)}
.section-title{left:135px;top:35px;font-size:18px;font-weight:400;color:var(--ink)}
.card{top:75px;width:150px;height:230px;border-radius:6px;background:rgba(238,249,250,.7);box-shadow:0 4px 12px rgba(0,0,0,.04);overflow:hidden}
.card-media{left:0;top:0;width:150px;height:150px}
.badge{left:7px;top:129px;height:15px;padding:0 8px;border-radius:8px;background:var(--ink);color:var(--white);font-size:7.5px;font-weight:500;display:flex;align-items:center}
.card-name{left:0;width:150px;top:168px;text-align:center;font-size:10px;color:var(--ink)}
.price-old{left:0;width:150px;top:188px;text-align:center;font-size:7.5px;color:var(--muted);text-decoration:line-through;letter-spacing:.2px}
.price{left:0;width:150px;top:200px;text-align:center;font-size:10px;color:var(--ink);letter-spacing:.3px}
.newsletter{left:0;top:932px;width:945px;height:198px;background:linear-gradient(180deg,var(--base) 0%,var(--tint) 55%,var(--base) 100%)}
.news-title{left:0;width:945px;top:28px;text-align:center;font-size:30px;font-weight:400;color:var(--ink)}
.news-copy{left:0;width:945px;top:79px;text-align:center;font-size:10px;color:var(--text);letter-spacing:.2px}
.email{left:362px;top:107px;width:221px;height:28px;border:1px solid var(--muted);border-radius:5px;background:rgba(255,255,255,.3);font-size:10px;color:var(--muted);padding-left:12px;display:flex;align-items:center}
.email svg{position:absolute;right:9px;top:9px}
.site-footer{left:0;top:1130px;width:945px;height:70px;border-top:1px solid var(--line);background:linear-gradient(180deg,var(--base),#eef5f6)}
.legal{left:135px;top:28px;font-size:7px;color:var(--muted);letter-spacing:.2px}
</style>
</head>
<body>
<div class="abs announcement">
  <svg style="left:137px" width="5" height="8" viewBox="0 0 5 8"><path d="M4 1L1 4l3 3" fill="none" stroke="#fff" stroke-width="1"/></svg>
  Welcome to our store
  <svg style="left:804px" width="5" height="8" viewBox="0 0 5 8"><path d="M1 1l3 3-3 3" fill="none" stroke="#fff" stroke-width="1"/></svg>
</div>

<header class="abs site-header">
  <div class="abs brand">Tavrix</div>
  <svg class="abs" style="left:739px;top:19px" width="14" height="14" viewBox="0 0 14 14"><circle cx="5.8" cy="5.8" r="4.6" fill="none" stroke="#2b2839" stroke-width="1.2"/><path d="M9.2 9.2L13 13" stroke="#2b2839" stroke-width="1.2"/></svg>
  <svg class="abs" style="left:766px;top:19px" width="14" height="14" viewBox="0 0 14 14"><circle cx="7" cy="4.5" r="3" fill="none" stroke="#2b2839" stroke-width="1.1"/><path d="M1.5 13c0-3 2.5-4.8 5.5-4.8s5.5 1.8 5.5 4.8z" fill="none" stroke="#2b2839" stroke-width="1.1"/></svg>
  <svg class="abs" style="left:793px;top:19px" width="14" height="14" viewBox="0 0 14 14"><path d="M1.5 4h11l-.8 9H2.3z" fill="none" stroke="#2b2839" stroke-width="1.1"/><path d="M4.5 4V3a2.5 2.5 0 015 0v1" fill="none" stroke="#2b2839" stroke-width="1.1"/></svg>
  <nav class="abs nav"><span class="current">Home</span><span>Shop</span><span>About us</span><span>Help</span><span>Blog</span></nav>
</header>

<section class="abs hero">
  <div class="abs hero-media"></div>
  <div class="abs hero-card"></div>
  <h1 class="abs hero-title">Strong<br>Feet,<br>Confident<br>Steps.</h1>
  <p class="abs hero-copy">Designed for comfort and support, it helps heal your foot and ankle injuries while keeping you mobile.</p>
  <div class="abs btn">Shop now</div>
  <div class="abs product-visual" role="img" aria-label="Product photo of a white walking boot with grey straps and teal sole"></div>
  <div class="abs feature" style="left:443px;top:59px">
    <svg width="22" height="22" viewBox="0 0 22 22"><path d="M3 20C6 12 12 5 20 2c0 8-6 13-14 14" fill="none" stroke="#33d1d3" stroke-width="1.2"/><path d="M3 20l10-11" stroke="#33d1d3" stroke-width="1"/></svg>
    Lightweight
  </div>
  <div class="abs feature" style="left:663px;top:145px">
    <svg width="16" height="22" viewBox="0 0 16 22"><circle cx="8" cy="3" r="2" fill="none" stroke="#33d1d3" stroke-width="1.1"/><path d="M8 6l-2 7 4 3 1 5M6 13l-3 8M7 8l-4 4M8 7l4 4" fill="none" stroke="#33d1d3" stroke-width="1.1"/></svg>
    Breathable
  </div>
  <div class="abs feature" style="left:409px;top:224px">
    <svg width="20" height="22" viewBox="0 0 20 22"><rect x="2" y="2" width="10" height="18" rx="1.5" fill="none" stroke="#33d1d3" stroke-width="1.1"/><path d="M16 1v20" stroke="#33d1d3" stroke-width="1.1"/><rect x="14" y="8" width="4" height="5" rx="1" fill="#f0fafa" stroke="#33d1d3" stroke-width="1.1"/></svg>
    Adjustable
  </div>
</section>

<section class="abs featured">
  <h2 class="abs section-title">Featured products</h2>
  <div class="abs card" style="left:135px">
    <div class="abs card-media" role="img" aria-label="White walking boot with teal sole" style="background:linear-gradient(180deg,#fff 0%,#e6e7ec 60%,#bfeff0 100%)"></div>
    <div class="abs badge">Sale</div>
    <div class="abs card-name">Smart Medical Boot</div>
    <div class="abs price-old">$500.00 USD</div>
    <div class="abs price">$350.00 USD</div>
  </div>
  <div class="abs card" style="left:310px">
    <div class="abs card-media" role="img" aria-label="Grey walking boot with black straps" style="background:linear-gradient(180deg,#f4f4f4 0%,#9a9ca3 60%,#dfe6e6 100%)"></div>
    <div class="abs badge">Sale</div>
    <div class="abs card-name">Smart Medical Boot 2</div>
    <div class="abs price-old">$500.00 USD</div>
    <div class="abs price">$350.00 USD</div>
  </div>
  <div class="abs card" style="left:485px">
    <div class="abs card-media" role="img" aria-label="Tall white walking boot" style="background:linear-gradient(180deg,#fff 0%,#e3e4e8 60%,#c4eff0 100%)"></div>
    <div class="abs badge">Sale</div>
    <div class="abs card-name">Smart Medical Boot 3</div>
    <div class="abs price-old">$500.00 USD</div>
    <div class="abs price">$350.00 USD</div>
  </div>
  <div class="abs card" style="left:660px">
    <div class="abs card-media" role="img" aria-label="Tall black walking boot" style="background:linear-gradient(90deg,#fff 20%,#2e2f33 50%,#fff 80%)"></div>
    <div class="abs badge">Sale</div>
    <div class="abs card-name">Smart Medical Boot 4</div>
    <div class="abs price-old">$500.00 USD</div>
    <div class="abs price">$350.00 USD</div>
  </div>
</section>

<section class="abs newsletter">
  <h2 class="abs news-title">Subscribe to our emails</h2>
  <p class="abs news-copy">Join our email list for exclusive offers and the latest news.</p>
  <div class="abs email">Email
    <svg width="10" height="8" viewBox="0 0 10 8"><path d="M0 4h9M6 1l3 3-3 3" fill="none" stroke="#2b2839" stroke-width="1"/></svg>
  </div>
</section>

<footer class="abs site-footer">
  <div class="abs legal">© 2024, tavrix1 Powered by Shopwell &nbsp;·&nbsp; Privacy policy</div>
</footer>
</body>
</html>
```